3D abstract logo Construction, Kitchen and Bath design and Project Management Business Card Design

I want a 3d abstract logo for a new General Construction, Kitchen and Bath design and Project Management Company located at Philadelphia RM, we want to put our logo in the white color trucks too. I want to look professional and serious at the same time look like an architect design and the warm originals color that make you feel in a nice decorated home, I like the colors trend in this link:
http://www.printmoxel.example/vp/nns/doceditor.aspx?alt_doc_id=QK31R-T7B52-4W2&doc_id=5813096421&pf_id=D4M

I was thinking about a roof and the RM font could have square shape or like wood framing with two tones of the brick color black and creamy yellow color.... Also I like the keystone Idea like the modification or the Lorvane Expressway logo but curvy at the top

The final design should communicate big company (because we want to grow), responsible, professional and organized that really care about our customers and give them everything they need... plan and design, excellent labor and Project Management
Updates

I doesn't have to be 3d

Reason: I haven't received enough options...

Please stick with the warm tones shown in the image001 attached I like spicy cinnamon instead a cold wine or brick color and also the cream yellowish tones added

Hello designers, please use only the idea and colors of the image001 I don't want to be stick with a house logo because I do commercial construction too so I prefer work around the keystone idea maybe leaving the style of the RM.
I'd like the base tone on the card dark like first option and you can send me a white option too.

Please send me your ideas as soon as possible 

Thank you so much!

Target Market(s)

Builders, State, commercial business owners, Property owners or Real State and Property Management Companies

Industry/Entity Type

Architect

Contact Information for Business Card

RM Builders LLC
“Every plan has a home”
Tessa Kolward Eng.
President
Commercial & Residential General Construction
Kitchen & Bath Design | Project Management
Phone: 555-307-4196 | Fax: 555-307-4197 Cell: 555-918-2630
tessa@rmbuildersco.example

```html
<!DOCTYPE html>
<html lang="en">
<head>
<meta charset="utf-8">
<title>RM Builders LLC – Business Card</title>
<link rel="stylesheet" href="https://fonts.googleapis.com/css2?family=Jost:ital,wght@0,400;0,600;1,400;1,600;1,700&display=swap">
<style>
  :root {
    --cream: #EFC777;
    --cinnamon: #A81E2A;
    --ink: #111111;
    --paper: #FFFFFF;
  }
  * { margin: 0; padding: 0; box-sizing: border-box; }
  html, body { width: 1200px; height: 702px; overflow: hidden; background: var(--paper); }
  .card {
    position: relative;
    width: 1200px;
    height: 702px;
    font-family: "Jost", "Futura", sans-serif;
    color: var(--ink);
  }
  .card__panels { position: absolute; inset: 0; }
  .panel--cream { fill: var(--cream); }
  .panel--cinnamon { fill: var(--cinnamon); }

  .wordmark {
    position: absolute;
    left: 0;
    top: 150px;
    width: 424px;
    text-align: center;
    font-size: 52px;
    font-weight: 600;
    color: var(--cinnamon);
    letter-spacing: 0.5px;
  }

  .person { position: absolute; left: 61px; top: 418px; }
  .person__name { font-size: 40px; font-weight: 700; font-style: italic; line-height: 1.1; }
  .person__title { font-size: 27px; font-style: italic; margin-top: 4px; }
  .person__email { position: absolute; left: 61px; top: 556px; font-size: 24px; font-style: italic; }
  .person__email strong { font-weight: 700; }

  .company { position: absolute; left: 564px; top: 112px; color: var(--paper); }
  .company__name { font-size: 49px; font-weight: 700; font-style: italic; line-height: 1.1; letter-spacing: 0.5px; }
  .company__tagline { font-size: 34px; font-weight: 700; font-style: italic; line-height: 1.2; }
  .company__services { margin-top: 20px; font-size: 24px; line-height: 1.2; }

  .contact { position: absolute; left: 570px; top: 480px; color: var(--paper); font-size: 25px; font-style: italic; line-height: 34px; }
  .contact__label { font-weight: 700; }
  .contact strong { font-weight: 700; }
</style>
</head>
<body>
<main class="card">
  <svg class="card__panels" width="1200" height="702" viewBox="0 0 1200 702" aria-hidden="true">
    <polygon class="panel--cream" points="0,0 542,0 424,74 424,693 0,693"/>
    <polygon class="panel--cinnamon" points="630,0 1200,0 1200,693 470,693 470,96"/>
  </svg>

  <div class="wordmark">RM Builders</div>

  <section class="person">
    <h1 class="person__name">Tessa Kolward</h1>
    <p class="person__title">President</p>
  </section>
  <p class="person__email"><strong>tessa@rmbuildersco</strong>.example</p>

  <section class="company">
    <h2 class="company__name">RM Builders LLC</h2>
    <p class="company__tagline">“Every plan has a home”</p>
    <p class="company__services">Commercial &amp; Residential General Construction<br>Kitchen &amp; Bath Design&nbsp; |&nbsp; Project Management</p>
  </section>

  <section class="contact">
    <p><span class="contact__label">Phone:</span> 555-307-4196</p>
    <p><span class="contact__label">Fax:</span> 555-307-4197</p>
    <p>www.<strong>rmbuildersco</strong>.example</p>
  </section>
</main>
</body>
</html>
```